Layout for new page on existing website

We have an existing website (www.brightloomworks.org) and need a new page designing to promote a new product.
The new page needs to be consistent with the existing website look and feel (www.brightloomworks.org) but current persistent elements on the standard page design can be moved/removed from the page to accommodate a new layout necessary for getting all the content laid out in a logical user friendly way.
The content required for the page is attached along with a wireframe mock up that may help understand the expectation, however the wireframe was just created to help me work out what was needed on the page and the layout can be different. A key element is the quality of the design of each of the artifacts (e.g. the panel the embedded video needs to go in, icons etc) and a clear display of the information.
Updates
The website that the new page needs to fit into is www.brightloomworks.org, i will also added the company logo to the brief.
Our Corporate Colours
- Green: #A2FF00
- Cream: #FFFF99
- Yellow: #FFE900
- Grey: #534741
Industry/Entity Type
Product
Look and feel
Each slider illustrates characteristics of the customer's brand and the style your logo design should communicate.

```html
<!DOCTYPE html>
<html lang="en">
<head>
<meta charset="utf-8">
<title>Brightloom Works – Course Management and Booking Simplified</title>
<link href="https://fonts.googleapis.com/css2?family=PT+Sans:ital,wght@0,400;0,700;1,400&display=swap" rel="stylesheet">
<style>
:root{
  --page-bg:#62574f;
  --panel:#ffffff;
  --bar:#ececec;
  --green:#8cc63f;
  --green-dark:#6a9e22;
  --brand-green:#a2ff00;
  --heading-grey:#8d8a86;
  --text:#555;
  --text-soft:#7a7a7a;
  --line:#dcdcdc;
  --field:#f7f7f7;
  --field-border:#cfcfcf;
  --btn:#1c1c1c;
}
*{box-sizing:border-box;margin:0;padding:0}
html,body{width:1200px;height:900px;overflow:hidden}
body{background:var(--page-bg);font-family:Arial,Helvetica,sans-serif;color:var(--text);position:relative}
.abs{position:absolute}
.heading{font-family:"PT Sans",Arial,sans-serif}

/* header */
.brand{left:390px;top:14px;display:flex;align-items:center;gap:6px;font-family:"PT Sans",Arial,sans-serif;font-weight:700;font-size:11px;letter-spacing:2px;color:#fff}
.brand-mark{width:16px;height:16px;border-radius:50%;background:var(--brand-green)}
.social{left:763px;top:20px;display:flex;align-items:center;gap:5px;font-family:"PT Sans",Arial,sans-serif;font-size:7px;color:#eee}
.social span.sq{width:9px;height:9px;background:#9aa6ad;display:inline-block}

/* main panel */
.main-panel{left:384px;top:47px;width:450px;height:345px;background:var(--panel);border-radius:4px;overflow:hidden}
.nav{height:18px;background:var(--bar);display:flex;align-items:center;gap:10px;padding-left:6px;font-family:"PT Sans",Arial,sans-serif;font-size:7px;font-weight:700;color:#555}
.nav .current{color:var(--green)}
.hero-art{left:9px;top:31px;width:127px;height:110px;background:linear-gradient(135deg,#f4f4f4,#e2e2e2)}
.hero-title{left:143px;top:31px;font-size:26px;line-height:27px;color:var(--heading-grey)}
.hero-copy{left:143px;top:92px;width:300px;font-size:6px;line-height:9.4px;color:var(--text)}
.divider{left:10px;top:149px;width:430px;height:1px;background:var(--line)}
.sub-title{top:157px;font-size:11px;font-style:italic;color:var(--heading-grey)}
.video-frame{left:11px;top:176px;width:209px;height:152px;background:#1b1b1b;border:1px solid #555}
.video-screen{left:0;top:0;width:207px;height:142px;background:linear-gradient(90deg,#1e1e1e 0 52%,#3d5b62 52% 100%)}
.video-controls{left:0;top:142px;width:207px;height:8px;background:#2c2c2c;border-top:1px solid #444}
.testimonials{left:230px;top:175px;width:211px;font-size:6px;line-height:9.4px;color:var(--text)}
.testimonial{margin-bottom:14px}
.cite{text-align:right;font-style:italic;color:var(--text-soft);margin-top:5px}
.cite a{color:var(--text-soft)}

/* sections */
.section-title{left:394px;font-size:15px;color:#fff}
.feature{width:210px;height:46px;background:var(--panel);border-radius:4px}
.feature svg{position:absolute;left:4px;top:6px}
.feature h3{position:absolute;left:40px;top:4px;font-family:"PT Sans",Arial,sans-serif;font-size:9.5px;color:#666}
.feature p{position:absolute;left:40px;top:18px;width:166px;font-size:6px;line-height:8.4px;color:var(--text)}
.feature a{position:absolute;right:6px;bottom:3px;font-size:5.5px;color:var(--green-dark)}
.benefits{left:394px;top:616px;width:430px;height:76px;background:var(--panel);border-radius:4px;padding:6px 8px;font-size:6px;line-height:9.3px;font-style:italic;color:#444}
.benefits p+p{margin-top:8px}

.quote-form{left:394px;top:724px;width:430px;height:108px;background:#e6e6e6;border-radius:5px;padding:4px}
.quote-inner{width:100%;height:100%;background:#ededed;border:1px solid #fff;border-radius:4px;position:relative}
.field-label{font-size:6.5px;color:#333}
.field{width:176px;height:16px;background:var(--field);border:1px solid var(--field-border);border-radius:2px}
.send{left:358px;top:78px;width:55px;height:15px;background:linear-gradient(#3a3a3a,var(--btn));border-radius:2px;color:#fff;font-size:8px;font-weight:700;text-align:center;line-height:15px}

.footer{left:384px;top:851px;width:450px;height:40px;background:var(--bar);border-radius:0 0 4px 4px;text-align:center}
.footer-nav{margin-top:11px;font-size:5.5px;color:#999;word-spacing:1px}
.footer-nav span{margin:0 4px}
.copyright{margin-top:9px;font-size:5px;color:#c4c4c4}
</style>
</head>
<body>

<header>
  <div class="abs brand"><span class="brand-mark"></span>BRIGHTLOOM WORKS</div>
  <div class="abs social">JOIN US: <span class="sq"></span><span class="sq"></span><span class="sq"></span></div>
</header>

<main class="abs main-panel">
  <nav class="nav"><span class="current">HOME</span><span>ABOUT US</span><span>OUR SERVICES</span><span>PORTFOLIO</span><span>TESTIMONIALS</span><span>CONTACT US</span></nav>

  <div class="abs hero-art" role="img" aria-label="Hand-drawn diagram of success linked to mentor, motivate, coach, inspire, teach, team work, vision and lead by example"></div>
  <h1 class="abs heading hero-title" style="font-weight:400">Course Management and<br>Booking Simplified</h1>
  <p class="abs hero-copy">We focus on you, delivering as early as possible so you are able to benefit from your ideas quickly, we do this with passion, pride, creativity and a conscience at a price that will make you smile. We are an honest, ethical and hard working team who push hard to deliver the best for our clients in a fun, interactive and creative environment. If we are able to help you in anyway, we will. You are the reason why we exist, we get a kick out of solving your problems or being part of your vision.</p>

  <div class="abs divider"></div>
  <h2 class="abs heading sub-title" style="left:11px;font-weight:400">Build with only your business in mind</h2>
  <h2 class="abs heading sub-title" style="left:230px;font-weight:400">Testimonials</h2>

  <div class="abs video-frame">
    <div class="abs video-screen" role="img" aria-label="Embedded product video showing a presentation title slide"></div>
    <div class="abs video-controls"></div>
  </div>

  <div class="abs testimonials">
    <div class="testimonial">
      <p>"Working with Brightloom Works brought a professional approach to our development process resulting in high quality software without the high cost and with the added bonus of working with some of the most dedicated people in the business, despite the timezone differences."</p>
      <p class="cite">Owen Hartley, Founder<br><a href="#">www.civicledger.com</a></p>
    </div>
    <div class="testimonial" style="margin-top:20px">
      <p>"Thanks to Brightloom Works our company has an exceptional website that is so easy to navigate around. Our customers love it and find it easy to use. Brightloom Works made the process simple to do and helped to launch us in a unique and practical way.<br>We will continue to work with them, helping our company embrace the lucrative space of social networking and advising us on getting the best out of the web"</p>
      <p class="cite">Clara Pennick, Director<br><a href="#">www.stepcoach.org.uk</a></p>
    </div>
  </div>
</main>

<h2 class="abs heading section-title" style="top:405px;font-weight:400">Key Features</h2>

<!-- feature cards -->
<div class="abs feature" style="left:394px;top:428px">
  <svg width="32" height="34" viewBox="0 0 32 34"><circle cx="20" cy="12" r="9" fill="var(--green)" stroke="#fff" stroke-width="2"/><circle cx="20" cy="12" r="3" fill="#fff"/><circle cx="9" cy="24" r="7" fill="var(--green)" stroke="#fff" stroke-width="2"/><circle cx="9" cy="24" r="2.5" fill="#fff"/></svg>
  <h3>We build web-based applications.</h3><p>We will manage everything that is needed to get your idea from a concept to a working product launched to your market.</p><a href="#">read more</a>
</div>
<div class="abs feature" style="left:614px;top:428px">
  <svg width="32" height="34" viewBox="0 0 32 34"><circle cx="20" cy="12" r="9" fill="var(--green)" stroke="#fff" stroke-width="2"/><circle cx="20" cy="12" r="3" fill="#fff"/><circle cx="9" cy="24" r="7" fill="var(--green)" stroke="#fff" stroke-width="2"/><circle cx="9" cy="24" r="2.5" fill="#fff"/></svg>
  <h3>We build web-based applications.</h3><p>We will manage everything that is needed to get your idea from a concept to a working product launched to your market.</p><a href="#">read more</a>
</div>
<div class="abs feature" style="left:394px;top:483px">
  <svg width="32" height="34" viewBox="0 0 32 34"><rect x="8" y="2" width="20" height="28" rx="2" fill="var(--green)"/><path d="M12 8h12M12 12h12M12 16h8" stroke="#fff" stroke-width="1.5"/><path d="M2 19h10v-4l7 7-7 7v-4H2z" fill="#fff" stroke="var(--green-dark)" stroke-width="1"/></svg>
  <h3>We make existing applications go faster.</h3><p>Migration work is laborious and time consuming but needs focus and attention to detail in every step of the process.</p><a href="#">read more</a>
</div>
<div class="abs feature" style="left:614px;top:483px">
  <svg width="32" height="34" viewBox="0 0 32 34"><rect x="8" y="2" width="20" height="28" rx="2" fill="var(--green)"/><path d="M12 8h12M12 12h12M12 16h8" stroke="#fff" stroke-width="1.5"/><path d="M2 19h10v-4l7 7-7 7v-4H2z" fill="#fff" stroke="var(--green-dark)" stroke-width="1"/></svg>
  <h3>We make existing applications go faster.</h3><p>Migration work is laborious and time consuming but needs focus and attention to detail in every step of the process.</p><a href="#">read more</a>
</div>
<div class="abs feature" style="left:394px;top:538px">
  <svg width="32" height="34" viewBox="0 0 32 34"><rect x="5" y="4" width="22" height="26" rx="3" fill="var(--green)"/><rect x="12" y="1" width="8" height="5" rx="1" fill="var(--green-dark)"/><rect x="9" y="9" width="14" height="16" fill="#fff"/><circle cx="16" cy="15" r="3" fill="var(--green)"/><rect x="11" y="19" width="10" height="4" rx="2" fill="var(--green)"/></svg>
  <h3>We establish offshore IT teams.</h3><p>Migration work is laborious and time consuming but needs focus and attention to detail in every step of the process.</p><a href="#">read more</a>
</div>
<div class="abs feature" style="left:614px;top:538px">
  <svg width="32" height="34" viewBox="0 0 32 34"><rect x="5" y="4" width="22" height="26" rx="3" fill="var(--green)"/><rect x="12" y="1" width="8" height="5" rx="1" fill="var(--green-dark)"/><rect x="9" y="9" width="14" height="16" fill="#fff"/><circle cx="16" cy="15" r="3" fill="var(--green)"/><rect x="11" y="19" width="10" height="4" rx="2" fill="var(--green)"/></svg>
  <h3>We establish offshore IT teams.</h3><p>Migration work is laborious and time consuming but needs focus and attention to detail in every step of the process.</p><a href="#">read more</a>
</div>

<h2 class="abs heading section-title" style="top:595px;font-weight:400">Benefits</h2>
<section class="abs benefits">
  <p>Brightloom Works is a web development company based in both the UK and India. Our core business is focused on the development and integration of web based systems that solve real world business problems for our clients' whether that be through the development of beautifully designed static websites or feature rich dynamic web applications and websites.</p>
  <p>We deliver quality driven value for money IT Solutions no matter the size of the project. By building transparent ethical partnerships with our customers and creating an exceptional working environment for our team we continue to retain and grow our workforce family whilst continuing to be the preferred web development provider for our customers.</p>
</section>

<h2 class="abs heading section-title" style="top:704px;font-weight:400">Get a free no obligation quote</h2>
<form class="abs quote-form">
  <div class="quote-inner">
    <label class="abs field-label" style="left:13px;top:11px">Name:</label>
    <div class="abs field" style="left:12px;top:22px"></div>
    <label class="abs field-label" style="left:242px;top:11px">Email:</label>
    <div class="abs field" style="left:241px;top:22px"></div>
    <label class="abs field-label" style="left:13px;top:46px">Company:</label>
    <div class="abs field" style="left:12px;top:57px"></div>
    <label class="abs field-label" style="left:242px;top:46px">Telephone:</label>
    <div class="abs field" style="left:241px;top:57px"></div>
    <div class="abs send">Send</div>
  </div>
</form>

<footer class="abs footer">
  <div class="footer-nav"><span>HOME</span><span>ABOUT US</span><span>OUR SERVICES</span><span>PORTFOLIO</span><span>TESTIMONIALS</span><span>CONTACT US</span></div>
  <div class="copyright">Copyright © 2011 Brightloom Works. All Rights Reserved. <u>Disclaimer</u></div>
</footer>

</body>
</html>
```